immediate money for financial solutions

We need a Clean yet, eye catching, Business Card denoting a professional financial/tech firm. The front should have our logo and the notion that we are money lenders that get business loans quickly & easily. Maybe shade the colors of our logo. We are opened, but not committed to an unusual shaped card. The Back Should have our Business Contact Info & logo found on our website's front page: KORVANTINC.COM

Financial

```html
<!DOCTYPE html>
<html lang="en">
<head>
<meta charset="utf-8">
<title>Korvant Inc — Business Card</title>
<link rel="stylesheet" href="https://fonts.googleapis.com/css2?family=Tinos:wght@400;700&display=swap">
<style>
  :root {
    --page-bg: #d4d4d4;
    --card-bg: #ffffff;
    --brand-green: #2a9a48;
    --brand-teal: #14967a;
    --leaf-green: #2fa347;
    --pattern-tint: #eef6f1;
    --card-shadow: rgba(0, 0, 0, 0.22);
  }
  * { box-sizing: border-box; margin: 0; padding: 0; }
  html, body {
    width: 1200px; height: 1000px; overflow: hidden;
    background: var(--page-bg);
    font-family: "Tinos", "Times New Roman", serif;
  }
  .canvas { position: relative; width: 1200px; height: 1000px; }

  .card {
    position: absolute; left: 300px; width: 600px; height: 343px;
    background: var(--card-bg);
    box-shadow: 0 8px 22px var(--card-shadow);
    overflow: hidden;
  }
  .card--front { top: 110px; }
  .card--back { top: 530px; }

  /* Front */
  .front-pattern {
    position: absolute; inset: 0;
    background: linear-gradient(135deg, #ffffff 0%, var(--pattern-tint) 50%, #ffffff 100%);
  }
  .brand-lockup {
    position: absolute; text-align: center; color: var(--brand-green);
  }
  .card--front .brand-lockup { left: 0; right: 0; top: 90px; }
  .brand-mark {
    display: block; width: 34px; height: 34px; margin: 0 auto 10px;
    background: var(--brand-green);
  }
  .brand-name {
    display: inline-block; font-size: 44px; font-weight: 400; line-height: 1;
    letter-spacing: 1px; padding: 0 6px 4px;
    border-bottom: 2px solid var(--brand-green);
  }
  .brand-tagline {
    display: block; font-size: 26px; line-height: 1.2; margin-top: 4px;
    color: var(--brand-teal); letter-spacing: 0.5px;
  }
  .front-url {
    position: absolute; left: 0; right: 0; bottom: 22px;
    text-align: center; font-size: 20px; color: var(--brand-green);
  }

  /* Back */
  .side-artwork {
    position: absolute; left: 0; top: 0; width: 190px; height: 343px;
    background: linear-gradient(160deg, var(--leaf-green) 0%, var(--brand-teal) 100%);
  }
  .card--back .brand-lockup { left: 270px; right: 20px; top: 14px; }
  .card--back .brand-mark { width: 28px; height: 28px; margin-bottom: 8px; }
  .card--back .brand-name { font-size: 38px; }
  .card--back .brand-tagline { font-size: 22px; }

  .holder {
    position: absolute; right: 48px; top: 162px; text-align: right;
    color: var(--brand-green);
  }
  .holder-name { font-size: 24px; font-weight: 700; }
  .holder-role { font-size: 15px; }

  .contact-list {
    position: absolute; left: 375px; top: 226px; list-style: none;
    color: var(--brand-green); font-size: 18px; line-height: 22px;
  }
  .contact-list li { display: flex; align-items: center; gap: 16px; }
  .contact-icon { width: 12px; height: 12px; flex: none; fill: var(--brand-green); }

  .affiliation {
    position: absolute; left: 205px; bottom: 12px;
    color: var(--brand-green); font-size: 16px; line-height: 20px;
  }
  .affiliation span { display: block; }
</style>
</head>
<body>
<main class="canvas">

  <section class="card card--front" aria-label="Card front">
    <div class="front-pattern" role="img" aria-label="Faint light green striped background pattern"></div>
    <div class="brand-lockup">
      <span class="brand-mark"></span>
      <span class="brand-name">KORVANT INC</span>
      <span class="brand-tagline">READY-SET-GO</span>
    </div>
    <p class="front-url">www.korvantinc.com</p>
  </section>

  <section class="card card--back" aria-label="Card back">
    <div class="side-artwork" role="img" aria-label="Decorative green and teal geometric artwork"></div>

    <div class="brand-lockup">
      <span class="brand-mark"></span>
      <span class="brand-name">KORVANT INC</span>
      <span class="brand-tagline">READY-SET-GO</span>
    </div>

    <div class="holder">
      <p class="holder-name">Daniel Marsh</p>
      <p class="holder-role">President / Lender</p>
    </div>

    <ul class="contact-list">
      <li>
        <svg class="contact-icon" viewBox="0 0 12 12" aria-hidden="true"><path d="M2 1l2 0 1 3-1.3 1a6 6 0 0 0 3.3 3.3L8 7l3 1 0 2c0 .6-.5 1-1 1C5 11 1 7 1 2c0-.5.4-1 1-1z"/></svg>
        <span>555-014-2298</span>
      </li>
      <li>
        <svg class="contact-icon" viewBox="0 0 12 12" aria-hidden="true"><path d="M1 3h10v6H1z"/><path d="M1 3l5 3.5L11 3" fill="none" stroke="#fff" stroke-width="1"/></svg>
        <span>daniel@korvantinc.com</span>
      </li>
      <li>
        <svg class="contact-icon" viewBox="0 0 12 12" aria-hidden="true"><circle cx="6" cy="6" r="5"/><path d="M1 6h10M6 1v10" stroke="#fff" stroke-width="1"/></svg>
        <span>www.korvantinc.com</span>
      </li>
    </ul>

    <p class="affiliation">
      <span>Partner of Norvel Co.</span>
      <span>Trusted Funding Source Quick Capital Lender</span>
    </p>
  </section>

</main>
</body>
</html>
```